Coldforge Prime manufacturing Project

We are looking at getting a brand new design for a new company that deals in selling stainless tubing and other stainless still products such as handrails, Spigots, Balustrade Fittings
Glass, Glass fittings and Aluminium Channels

We require a very clean website that deals with the following colours:

Blue to light blues
Blacks
Greys to light Greys
Whites

We are open for other ideas BUT we *DO NOT* want any pinks, greens or bright colours except for backgrounds colours we have chosen above. (It can be solid, gradient or a subtle pattern)

YOU MUST KEEP THE LOGO AS IS. PLEASE DO NOT ALTER THE LOGO IN *ANY WAY* and the logo MUST be the same colours and fonts.

Logo is attached.

The site must contain these aspects:
jQuery Slider (Image slide show)
Top drop down Menus
Be no more than 900px wide
Text is to be to the w3C standards. (no special fonts)

We will chop up the design into html format. You just need to provide the PSD file.

The clients opposition is:
www.quorvatrim.example

Industry/Entity Type

It Company

Requirements
Nice to have
• Alter the logo in anyway

Files

```html
<!DOCTYPE html>
<html lang="en">
<head>
<meta charset="utf-8">
<title>Coldforge Prime — Stainless Steel Products</title>
<link href="https://fonts.googleapis.com/css2?family=Open+Sans:ital,wght@0,400;0,600;0,700;1,700&display=swap" rel="stylesheet">
<style>
:root{
  --blue:#5a80b6;
  --blue-dark:#4a78b4;
  --nav-top:#86b2df;
  --nav-bottom:#4d86c4;
  --ink:#333;
  --text:#555;
  --black:#000;
  --card:#3a3d42;
  --card-light:#4b4f55;
  --footer:#343434;
  --footer-text:#9a9a9a;
  --base:#222;
  --line:#e3e3e3;
}
*{margin:0;padding:0;box-sizing:border-box}
html,body{width:1036px;height:1200px;overflow:hidden;background:#fff}
body{position:relative;font-family:"Open Sans",Arial,sans-serif;color:var(--text)}
.abs{position:absolute}

/* header */
.brand{left:85px;top:14px;width:120px;text-align:center}
.brand-mark{display:block;margin:0 auto;width:68px;height:68px;border-radius:50%;background:#4a6f9e;border:4px solid #2d2d2d}
.brand-name{display:block;margin-top:6px;font-size:14px;color:#222;white-space:nowrap}
.brand-sub{display:block;font-size:6px;color:#222;letter-spacing:1px;white-space:nowrap}
.support{left:772px;top:20px}
.support-label{position:absolute;left:45px;top:0;font-size:11.5px;color:#333;white-space:nowrap}
.support-phone{position:absolute;left:45px;top:13px;font-size:20px;color:var(--blue);white-space:nowrap}
.follow{left:799px;top:74px;font-size:12px;color:#222}
.social-sq{top:70px;width:25px;height:25px;border-radius:3px;background:linear-gradient(#5fa3dc,#2c6fb0)}

/* nav */
.nav{left:0;top:122px;width:1036px;height:38px;background:linear-gradient(var(--nav-top),var(--nav-bottom))}
.nav a{position:absolute;top:9px;font-size:15.5px;font-weight:600;color:#fff;text-decoration:none;white-space:nowrap}

/* hero band */
.band{left:0;top:160px;width:1036px;height:405px;background:var(--black)}
.hero{left:85px;top:165px;width:867px;height:298px;background:linear-gradient(100deg,#8a7866 0%,#d9cfc3 35%,#b89e7e 55%,#e8e3dc 80%,#f1efec 100%)}
.hero-caption{left:570px;top:439px;width:382px;height:25px}
.hero-caption span{position:absolute;right:12px;top:1px;font-size:18px;font-weight:700;font-style:italic;color:#fff;white-space:nowrap}
.feature{top:473px;width:278px;height:84px;background:linear-gradient(90deg,var(--card-light),var(--card))}
.feature-img{position:absolute;left:0;top:0;width:101px;height:84px}
.feature h3{position:absolute;left:110px;top:6px;font-size:19.5px;font-weight:600;color:#fff}
.feature p{position:absolute;left:111px;top:37px;width:160px;font-size:10.3px;line-height:15px;color:#fff}

/* product boxes */
.product{top:593px;width:282px;height:108px;border:1px solid #d4d4d4;border-radius:3px;background:linear-gradient(#f2f2f2,#fff 45%,#ddd)}
.product h3{position:absolute;left:19px;top:12px;font-size:19.5px;font-weight:600;line-height:23px;color:var(--blue)}
.product p{position:absolute;left:19px;top:65px;font-size:11px;color:#777;white-space:nowrap}
.product-img{position:absolute;right:26px;top:18px;width:66px;height:66px;border-radius:6px;background:radial-gradient(#c8c8c8,#8d8d8d)}

/* content */
.welcome{left:85px;top:722px;width:578px}
.welcome h2,.testimonial h2{font-size:25.5px;font-weight:400;color:var(--ink);margin-bottom:10px}
.welcome p{font-size:11.4px;line-height:16px;color:#555;margin-bottom:16px}
.testimonial{left:672px;top:722px;width:248px}
.t-item{position:relative;height:60px;border-bottom:1px solid var(--line);font-family:Arial,sans-serif;font-size:11.3px;line-height:15px;color:#333}
.t-item:last-child{border-bottom:0}
.t-avatar{position:absolute;left:4px;top:3px;width:29px;height:29px;background:linear-gradient(#c9b08f,#8e7257)}
.t-text{position:absolute;left:40px;top:0;width:210px}
.t-text a{color:var(--blue-dark);text-decoration:none}

/* footer */
.footer{left:0;top:966px;width:1036px;height:183px;background:var(--footer);background-image:repeating-linear-gradient(45deg,rgba(255,255,255,.025) 0 2px,transparent 2px 5px)}
.f-col{position:absolute;top:22px}
.f-col h4{font-size:15.5px;font-weight:600;color:#fff;margin-bottom:8px}
.f-col li{list-style:none;font-size:10.6px;line-height:18.8px;color:var(--footer-text);white-space:nowrap}
.base{left:0;top:1149px;width:1036px;height:51px;background:var(--base)}
.copy{position:absolute;left:84px;top:17px;font-family:Arial,sans-serif;font-size:11.5px;color:#aaa}
.dot{position:absolute;top:14px;width:22px;height:22px;border-radius:50%;background:#6d6d6d}
</style>
</head>
<body>

<header>
  <div class="abs brand">
    <span class="brand-mark"></span>
    <span class="brand-name">Coldforge Prime</span>
    <span class="brand-sub">Manufacturing Co. Ltd</span>
  </div>

  <div class="abs support">
    <svg width="38" height="38" viewBox="0 0 38 38" aria-hidden="true">
      <path d="M6 20a13 13 0 0 1 26 0" fill="none" stroke="#222" stroke-width="3"/>
      <rect x="3" y="18" width="7" height="12" rx="2" fill="#222"/>
      <rect x="28" y="18" width="7" height="12" rx="2" fill="#222"/>
      <path d="M31 30q0 6-10 6" fill="none" stroke="#222" stroke-width="2"/>
      <circle cx="20" cy="36" r="2" fill="#222"/>
    </svg>
    <span class="support-label">24/7 SALES SUPPORT</span>
    <span class="support-phone">0800-555-0147</span>
  </div>
  <div class="abs follow">Follow Us</div>
  <span class="abs social-sq" style="left:869px"></span>
  <span class="abs social-sq" style="left:897px"></span>
  <span class="abs social-sq" style="left:925px"></span>
</header>

<nav class="abs nav">
  <a href="#" style="left:93px">Home</a>
  <a href="#" style="left:171px">About Us</a>
  <a href="#" style="left:272px">Products</a>
  <a href="#" style="left:370px">Services</a>
  <a href="#" style="left:463px">Woh We Are</a>
  <a href="#" style="left:585px">Contact Us</a>
</nav>

<section>
  <div class="abs band"></div>
  <div class="abs hero" role="img" aria-label="Marble staircase with stainless steel handrails"></div>
  <div class="abs hero-caption">
    <svg width="382" height="25" viewBox="0 0 382 25" aria-hidden="true"><polygon points="24,0 382,0 382,25 0,25" fill="#000"/></svg>
    <span>Primary Source For Stainless Steel Products</span>
  </div>

  <div class="abs feature" style="left:85px">
    <div class="feature-img" role="img" aria-label="Stainless steel handrail on a staircase" style="background:linear-gradient(120deg,#b9c3cc,#d7b18a 60%,#8c6a4d)"></div>
    <h3>Handrails</h3>
    <p>Lorem ipsum dolor sit amet consectetur adipisicing elit, lorem ipsum dolor</p>
  </div>
  <div class="abs feature" style="left:380px">
    <div class="feature-img" role="img" aria-label="Glass walled corridor" style="background:linear-gradient(90deg,#2e4a5e,#8fb6cc 50%,#2e4a5e)"></div>
    <h3>Glass</h3>
    <p>Lorem ipsum dolor sit amet consectetur adipisicing elit, lorem ipsum dolor</p>
  </div>
  <div class="abs feature" style="left:674px">
    <div class="feature-img" role="img" aria-label="Stainless steel spigot holding a glass panel" style="background:linear-gradient(140deg,#3d3f40,#b5b9b8 50%,#6f8f85)"></div>
    <h3>Spigots</h3>
    <p>Lorem ipsum dolor sit amet consectetur adipisicing elit, lorem ipsum dolor</p>
  </div>
</section>

<section>
  <div class="abs product" style="left:85px">
    <h3>Balustrade<br>Fittings</h3>
    <p>Lorem ipsum dolor sit amet</p>
    <div class="product-img" role="img" aria-label="Stainless balustrade fitting"></div>
  </div>
  <div class="abs product" style="left:381px">
    <h3>Glass<br>Fittings</h3>
    <p>Lorem ipsum dolor sit amet</p>
    <div class="product-img" role="img" aria-label="Glass standoff fitting"></div>
  </div>
  <div class="abs product" style="left:672px">
    <h3>Aluminium<br>Channels</h3>
    <p>Lorem ipsum dolor sit amet</p>
    <div class="product-img" role="img" aria-label="Aluminium channel profile"></div>
  </div>
</section>

<main>
  <article class="abs welcome">
    <h2>Welcome To Coldforge Prime</h2>
    <p>Lorem Ipsum is simply dummy text of the printing and typesetting industry. Lorem Ipsum has been the industry's standard dummy text ever since the 1500s, when an unknown printer took a galley of type and scrambled it to make a type specimen book.</p>
    <p>It has survived not only five centuries, but also the leap into electronic typesetting, remaining essentially unchanged. It was popularised in the 1960s with the release of Letraset sheets containing Lorem Ipsum passages, and more recently with desktop publishing software like Aldus PageMaker including versions of Lorem Ipsum.</p>
    <p>when an unknown printer took a galley of type and scrambled it to make a type specimen book.</p>
  </article>

  <aside class="abs testimonial">
    <h2>Testimonial</h2>
    <div class="t-item">
      <div class="t-avatar" role="img" aria-label="Member portrait"></div>
      <div class="t-text"><a href="#">Dorian VELESCU</a> posted the job ad <a href="#">"Senior Solutions..."</a> in the Jobs Section.<br><a href="#">jobs</a></div>
    </div>
    <div class="t-item" style="padding-top:0;margin-top:4px">
      <div class="t-avatar" role="img" aria-label="Member portrait"></div>
      <div class="t-text"><a href="#">Lisette Morand</a> is organizing the <a href="#">"Becoming a General..."</a> event.<br><a href="#">Events</a> | <a href="#">Frankfurt</a></div>
    </div>
    <div class="t-item" style="margin-top:4px">
      <div class="t-avatar" role="img" aria-label="Member portrait"></div>
      <div class="t-text"><a href="#">Lisette Morand</a> is organizing the <a href="#">"Becoming a General..."</a> event.<br><a href="#">Events</a> | <a href="#">Frankfurt</a></div>
    </div>
  </aside>
</main>

<footer>
  <div class="abs footer">
    <div class="f-col" style="left:85px"><h4>Home</h4><ul><li>How it Works</li><li>Benefits for Coldforge</li><li>Benefits for Coldforge</li><li>Join as Coldforge</li><li>Join as Coldforge Prime</li><li>FAQs</li></ul></div>
    <div class="f-col" style="left:293px"><h4>Links</h4><ul><li>Lorem ipsum</li><li>&nbsp;Dolor sit amet</li></ul></div>
    <div class="f-col" style="left:472px"><h4>Our Service</h4><ul><li>Search for Project</li><li>Submit Proposals</li><li>View Proposals</li><li>Edit Profile</li></ul></div>
    <div class="f-col" style="left:646px"><h4>About Us</h4><ul><li>News</li><li>Terms and Condition</li><li>Impressum</li><li>Contact Us</li></ul></div>
    <div class="f-col" style="left:836px"><h4>Contact Us</h4><ul><li>Lorem ipsum 124</li><li>Street 24</li><li>Call Now:0800-555-0147</li><li>info@coldforge.example</li></ul></div>
  </div>
  <div class="abs base">
    <span class="copy">Copyright © 2013 Coldforge. All rights reserved.</span>
    <span class="dot" style="left:766px"></span>
    <span class="dot" style="left:794px"></span>
    <span class="dot" style="left:823px"></span>
    <span class="dot" style="left:851px"></span>
    <span class="dot" style="left:879px"></span>
    <span class="dot" style="left:907px"></span>
    <span class="dot" style="left:936px"></span>
  </div>
</footer>

</body>
</html>
```